Zuvto..Hydrating sports energy drink

"Zuvto" is a hydrating, all-natural energy beverage geared towards health focused consumers and athletes
While other energy drinks are carbonated and artificially flavored, Zuvto's
light and refreshing all-natural formula tastes more like a sports drink without the heavy after effects
Zuvto's tropical, vitamin rich taste provides the hydration and burst of energy to help you perform at your best with out the calories....

Target Market(s)

hispanic males teen to 24 yrs old -with a cross over to the 18-35 yr old female due to it all-natural formula low in calories no sugar
this is a logo and bottle package design request. We have left it open to the arist vision
on how will look.

Thank you..Good luck!!!

Industry/Entity Type

Health

Requirements
Nice to have
• contrasting image ,

Several ideas have been submitted which look pretty good .

I like to have a contrasting design done as follows :

Think of a Spartan warrior caricature holding a shield in one hand , on the shield is our brand name Zuveto
.. in the other hand he is holding a lighting bolt he is standing on a bluff over looking a clear refreshing looking lake

```html
<!DOCTYPE html>
<html lang="en">
<head>
<meta charset="utf-8">
<title>Zuvto bottle design</title>
<link rel="stylesheet" href="https://fonts.googleapis.com/css2?family=Michroma&display=swap">
<style>
  :root {
    --page-bg: #ffffff;
    --outline: #111111;
    --tagline-ink: #111111;
    --claim-ink: #ffffff;
    --brand-ink: #f7e51c;
  }
  html, body {
    margin: 0;
    padding: 0;
    width: 1200px;
    height: 1000px;
    overflow: hidden;
    background: var(--page-bg);
  }
  .canvas {
    display: block;
    width: 1200px;
    height: 1000px;
  }
  .bottle-outline {
    fill: none;
    stroke: var(--outline);
    stroke-width: 2.5;
    stroke-linejoin: round;
  }
  .bottle-rule {
    stroke: var(--outline);
    stroke-width: 2;
    fill: none;
  }
  .thread {
    stroke: #000;
    stroke-width: 2;
    fill: none;
    opacity: 0.7;
  }
  .tagline {
    font-family: "Michroma", sans-serif;
    font-size: 22px;
    font-weight: 400;
    fill: var(--tagline-ink);
  }
  .brand-name {
    font-family: "Michroma", sans-serif;
    font-size: 64px;
    font-weight: 400;
    fill: var(--brand-ink);
  }
  .claim {
    font-family: "Michroma", sans-serif;
    font-size: 24px;
    font-weight: 400;
    fill: var(--claim-ink);
  }
</style>
</head>
<body>
<svg class="canvas" viewBox="0 0 1200 1000" xmlns="http://www.w3.org/2000/svg">
  <defs>
    <path id="bottle-shape" d="M520,44 Q520,40 524,40 L676,40 Q680,40 680,44 L680,158 L697,165 L700,300 C700,330 752,345 755,400 L756,440 Q756,452 748,458 Q740,465 748,472 L752,478 L752,855 Q744,866 752,874 L756,878 Q758,882 758,890 L758,945 Q758,955 748,955 L452,955 Q442,955 442,945 L442,890 Q442,882 446,878 L448,874 Q456,866 448,855 L448,478 L452,472 Q460,465 452,458 Q444,452 444,440 L445,400 C448,345 500,330 500,300 L503,165 L520,158 Z"/>
    <clipPath id="bottle-clip"><use href="#bottle-shape"/></clipPath>
    <linearGradient id="wrap-base" x1="0" y1="0" x2="0" y2="1">
      <stop offset="0" stop-color="#1a1a1a"/>
      <stop offset="0.15" stop-color="#3b332b"/>
      <stop offset="0.3" stop-color="#c27a20"/>
      <stop offset="0.45" stop-color="#e8c11c"/>
      <stop offset="0.62" stop-color="#c7c41e"/>
      <stop offset="0.76" stop-color="#4e982d"/>
      <stop offset="0.9" stop-color="#1f4c44"/>
      <stop offset="1" stop-color="#16302d"/>
    </linearGradient>
    <linearGradient id="wrap-sweep" x1="0" y1="0" x2="1" y2="0.4">
      <stop offset="0" stop-color="#e0661a" stop-opacity="0.55"/>
      <stop offset="0.5" stop-color="#f4e04a" stop-opacity="0.15"/>
      <stop offset="1" stop-color="#2a7f6a" stop-opacity="0.45"/>
    </linearGradient>
    <path id="tagline-arc" d="M455,437 Q603,418 752,437"/>
  </defs>

  <g class="bottle">
    <g clip-path="url(#bottle-clip)" role="img" aria-label="Abstract energy burst artwork in black, orange, yellow and green wrapping the bottle">
      <rect x="430" y="30" width="340" height="940" fill="url(#wrap-base)"/>
      <rect x="430" y="30" width="340" height="940" fill="url(#wrap-sweep)"/>
    </g>

    <g class="neck-threads">
      <path class="thread" d="M516,62 L684,62"/>
      <path class="thread" d="M512,82 L688,82"/>
      <path class="thread" d="M512,102 L688,102"/>
      <path class="thread" d="M506,124 Q600,132 694,124"/>
      <path class="thread" d="M506,134 Q600,142 694,134"/>
    </g>

    <use class="bottle-outline" href="#bottle-shape"/>
    <path class="bottle-rule" d="M452,458 L748,458"/>
    <path class="bottle-rule" d="M452,472 L748,472"/>
    <path class="bottle-rule" d="M448,478 L752,478"/>
    <path class="bottle-rule" d="M448,855 L752,855"/>
    <path class="bottle-rule" d="M448,874 L752,874"/>
    <path class="bottle-rule" d="M446,878 L754,878"/>

    <text class="tagline">
      <textPath href="#tagline-arc" startOffset="50%" text-anchor="middle" textLength="292" lengthAdjust="spacingAndGlyphs">ALL-NATURAL ENERGY</textPath>
    </text>

    <text class="brand-name" x="603" y="680" text-anchor="middle" textLength="270" lengthAdjust="spacingAndGlyphs">Zuvto</text>

    <text class="claim" x="604" y="822" text-anchor="middle" textLength="252" lengthAdjust="spacingAndGlyphs">VITAMIN RICH</text>
  </g>
</svg>
</body>
</html>
```